I am looking for a poster design with a pledge for my clients to take. The pledge will be to not use tanning beds. Our company is a Spray Tanning Salon that focuses on educating our clients on the dangers of indoor tanning while offering a safe alternative through spray tanning. I have an outline of a possible wording but I am VERY open to adjustments on it!
This is not a promotional poster. This is a poster that will be hanging in the salon and our clients will sign around the wall.
Updates

Project Deadline Extended Reason: Not currently in love with any submissions and would like to see more. Looking for a more simple design overall. Added Friday, October 28, 2016

Target Market(s)

Women 20-30 years old

Industry/Entity Type

Salon

Font styles to use
Sans Serif

Requirements
Must have
• Take the pledge to ditch the bed!
• Bellmont Glow Studio
• **Overall simple design, yet eye catching is requested. Not so busy**
Nice to have
• I am open to different wording!
• I pledge to be timeless
• -UVA rays in tanning beds cause wrinkles and other signs of premature aging
• I pledge to be fearless
• -Using tanning beds can cause severe eye damage, a weakened immune system, and melanoma the deadliest form of skin cancer.
• I pledge to be Sunless!
• -Join the PureHue revolution at Bellmont Glow Studio, Grand Rapids first Sunless Spa Experience.
Should not have
• The photo of the salon on it. I included that photo simply for reference of design, this is where this poster will be hung.

```html
<!DOCTYPE html>
<html lang="en">
<head>
<meta charset="utf-8">
<title>Take the Pledge – Bellmont Glow Studio</title>
<link href="https://fonts.googleapis.com/css2?family=Josefin+Sans:wght@300;600&family=Space+Mono:ital@0;1&display=swap" rel="stylesheet">
<style>
  :root {
    --paper: #ffffff;
    --pink: #ec1f7a;
    --lime: #c9dc2c;
    --salmon: #f26a6a;
    --ink: #2a2a2a;
    --white: #ffffff;
    --purple: #7a4fa3;
    --green: #7dc242;
    --sky: #8fc3e6;
    --blush: #f5a3c7;
    --orange: #f7a34a;
    --amber: #f39c3a;
    --yellow: #e7e34a;
  }
  html, body {
    margin: 0;
    padding: 0;
    overflow: hidden;
    background: var(--paper);
  }
  .poster {
    position: relative;
    width: 846px;
    height: 1200px;
    background: var(--paper);
    overflow: hidden;
  }
  .poster__art {
    position: absolute;
    inset: 0;
    width: 846px;
    height: 1200px;
  }
  .pledge-headline,
  .pledge-lead,
  .pledge-word,
  .pledge-fact,
  .pledge-cta,
  .brand-name {
    position: absolute;
    left: 77px;
    width: 698px;
    margin: 0;
    text-align: center;
  }
  .pledge-headline {
    top: 34px;
    font-family: "Josefin Sans", sans-serif;
    font-weight: 600;
    font-size: 30px;
    line-height: 1.2;
    letter-spacing: 1px;
    color: var(--pink);
  }
  .pledge-lead {
    font-family: "Space Mono", monospace;
    font-style: italic;
    font-size: 17px;
    line-height: 1.3;
    color: var(--ink);
    letter-spacing: 1px;
  }
  .pledge-word {
    font-family: "Josefin Sans", sans-serif;
    font-weight: 300;
    font-size: 96px;
    line-height: 1;
    letter-spacing: 2px;
    color: var(--white);
  }
  .pledge-fact {
    font-family: "Space Mono", monospace;
    font-style: italic;
    color: var(--ink);
    line-height: 1.3;
  }
  .pledge-fact--aging { font-size: 20px; letter-spacing: 1px; }
  .pledge-fact--health { font-size: 15.5px; letter-spacing: 0.4px; }
  .pledge-cta {
    font-family: "Space Mono", monospace;
    font-style: italic;
    font-size: 20px;
    line-height: 1.35;
    letter-spacing: 0.5px;
    color: var(--ink);
  }
  .brand-name {
    top: 1102px;
    font-family: "Space Mono", monospace;
    font-size: 22px;
    color: var(--ink);
  }
</style>
</head>
<body>
<main class="poster">
  <svg class="poster__art" viewBox="0 0 846 1200" xmlns="http://www.w3.org/2000/svg">
    <rect class="panel" x="77" y="125" width="698" height="959" fill="var(--pink)"/>

    <g class="hourglass">
      <polygon points="290,338 570,338 433,580" fill="var(--salmon)"/>
      <polygon points="433,580 280,800 570,800" fill="var(--salmon)"/>
      <polygon points="298,343 576,343 439,580" fill="var(--lime)"/>
      <polygon points="439,580 286,794 580,794" fill="var(--lime)"/>
    </g>

    <g class="accent-triangles" opacity="0.85">
      <polygon role="img" aria-label="Purple hatched triangle accent" points="139,103 44,268 234,268" fill="var(--purple)"/>
      <polygon role="img" aria-label="Green dotted triangle accent" points="596,93 818,93 705,262" fill="var(--green)"/>
      <polygon role="img" aria-label="Light blue striped triangle accent" points="735,321 669,430 798,430" fill="var(--sky)"/>
      <polygon role="img" aria-label="Soft pink dashed triangle accent" points="197,423 197,604 40,512" fill="var(--blush)"/>
      <polygon role="img" aria-label="Orange striped triangle accent" points="556,461 709,461 633,596" fill="var(--orange)"/>
      <polygon role="img" aria-label="Orange dashed triangle accent" points="689,685 576,866 806,866" fill="var(--amber)"/>
      <polygon role="img" aria-label="Yellow dotted triangle accent" points="165,955 48,1128 266,1128" fill="var(--yellow)"/>
    </g>

    <g class="swashes" fill="none" stroke="var(--white)" stroke-width="3" stroke-linecap="round">
      <path d="M120 222 C150 232 185 232 212 220"/>
      <path d="M642 220 C670 200 705 192 740 204"/>
      <path d="M120 562 C150 572 185 572 212 560"/>
      <path d="M642 560 C670 540 705 532 740 544"/>
      <path d="M130 910 C160 920 195 920 222 908"/>
      <path d="M632 908 C660 888 695 880 730 892"/>
    </g>
  </svg>

  <h1 class="pledge-headline">Take the pledge to ditch the bed!</h1>

  <p class="pledge-lead" style="top:130px;">I pledge to be</p>
  <h2 class="pledge-word" style="top:160px;">timeless</h2>
  <p class="pledge-fact pledge-fact--aging" style="top:270px;">UVA rays in tanning beds cause wrinkles and other<br>signs of premature aging</p>

  <p class="pledge-lead" style="top:465px;">I pledge to be</p>
  <h2 class="pledge-word" style="top:500px;">fearless</h2>
  <p class="pledge-fact pledge-fact--health" style="top:640px;">Using tanning beds can cause severe eye damage, a weakened immune<br>system and melanoma (the deadliest form of skin cancer)</p>

  <p class="pledge-lead" style="top:812px;">I pledge to be</p>
  <h2 class="pledge-word" style="top:848px;">sunless</h2>
  <p class="pledge-cta" style="top:975px;">Join the PureHue revolution at Bellmont Glow Studio;<br>Grand Rapids’ first sunless spa experience!</p>

  <p class="brand-name">Bellmont Glow Studio</p>
</main>
</body>
</html>
```